Car Wrap Design - Korvanteko Weldar Dual Cab Ute

We need a car wrap for a 2018 Korvanteko Weldar Ute - Dual Cab with Canopy. It's Used as a security and medical response vehicle.
Professional Look and finish needed.
Style guide attached.
Must have the words "Security & Medical Response"
Must have brellicanworksgroup.com
Must have phone number at rear 1800 392 816
Must have logo and company name
car image att

Industry/Entity Type

Security, Safety and Medical Response

Other font styles liked:
• Style Guide Att

Requirements
Must have
• Company Name, Website and Phone number. Must have words "Security & Medical Response"

```html
<!DOCTYPE html>
<html lang="en">
<head>
<meta charset="utf-8">
<title>Brellican Works – Ute Wrap Layouts</title>
<link rel="stylesheet" href="https://fonts.googleapis.com/css2?family=Montserrat:wght@600;700&family=Saira+Condensed:wght@600&display=swap">
<style>
  :root {
    --paper: #ffffff;
    --body-white: #eef1f0;
    --body-edge: #c9cfcd;
    --glass: #2f3537;
    --wrap-green: #2fa64a;
    --wrap-black: #1d1d1d;
    --ink: #1f1f1f;
    --on-dark: #ffffff;
  }
  html, body {
    margin: 0;
    padding: 0;
    width: 1200px;
    height: 1200px;
    overflow: hidden;
    background: var(--paper);
  }
  .wrap-sheet { display: block; width: 1200px; height: 1200px; }
  .panel-body { fill: var(--body-white); stroke: var(--body-edge); stroke-width: 1.5; }
  .glass { fill: var(--glass); }
  .canopy-seam { stroke: var(--wrap-black); stroke-width: 3; }
  .band-green { fill: var(--wrap-green); }
  .band-black { fill: var(--wrap-black); }
  .brand-name {
    font-family: "Montserrat", sans-serif;
    font-weight: 700;
  }
  .brand-name--dark { fill: var(--ink); }
  .brand-name--light { fill: var(--on-dark); }
  .brand-dot { fill: var(--wrap-green); }
  .tagline {
    font-family: "Saira Condensed", sans-serif;
    font-weight: 600;
    font-size: 17px;
    letter-spacing: 2.6px;
    fill: var(--ink);
  }
  .contact-line {
    font-family: "Montserrat", sans-serif;
    font-weight: 700;
    font-size: 13.5px;
  }
  .contact-line--light { fill: var(--on-dark); }
  .contact-line--dark { fill: var(--ink); }
  .contact-web { font-weight: 600; font-size: 11px; }
  .rear-mark { fill: none; stroke: #2a2a2a; stroke-width: 10; }
</style>
</head>
<body>
<svg class="wrap-sheet" viewBox="0 0 960 960" xmlns="http://www.w3.org/2000/svg" role="img" aria-label="Two side-view wrap layouts for a dual cab ute with canopy">
  <defs>
    <clipPath id="ute-side">
      <path d="M22,250 Q40,215 110,205 L240,198 L330,135 Q340,128 360,128 L600,128 Q612,130 615,140 L618,118 Q620,112 640,112 L900,112 Q915,114 918,130 L925,205 L932,210 L932,340 L760,345 A78,78 0 0 0 605,352 L235,355 A80,80 0 0 0 80,345 L30,330 Z"/>
    </clipPath>
  </defs>

  <!-- Layout A: white body with green sweep and black rear -->
  <g class="layout layout--sweep">
    <path class="panel-body" d="M22,250 Q40,215 110,205 L240,198 L330,135 Q340,128 360,128 L600,128 Q612,130 615,140 L618,118 Q620,112 640,112 L900,112 Q915,114 918,130 L925,205 L932,210 L932,340 L760,345 A78,78 0 0 0 605,352 L235,355 A80,80 0 0 0 80,345 L30,330 Z"/>
    <path class="glass" d="M268,200 L338,142 L430,140 L430,218 Z M440,140 L590,140 L596,212 L440,218 Z"/>
    <rect class="glass" x="660" y="124" width="212" height="70" rx="8"/>
    <line class="canopy-seam" x1="615" y1="206" x2="925" y2="206"/>
    <g clip-path="url(#ute-side)">
      <rect class="band-black" x="640" y="274" width="300" height="90"/>
      <path class="band-green" d="M230,328 L592,328 Q622,258 700,250 L940,250 L940,276 L712,276 Q656,284 636,360 L230,360 Z"/>
    </g>
    <text class="tagline" x="745" y="225" text-anchor="middle">SECURITY &amp; MEDICAL</text>
    <text class="tagline" x="745" y="244" text-anchor="middle">RESPONSE</text>
    <circle class="brand-dot" cx="270" cy="290" r="17"/>
    <text class="brand-name brand-name--dark" x="296" y="300" font-size="36">BRELLICAN</text>
    <text class="brand-name brand-name--dark" x="298" y="324" font-size="21" letter-spacing="8">WORKS</text>
    <text class="contact-line contact-line--light" x="252" y="348">1800 392 816 <tspan dx="4">|</tspan><tspan class="contact-web" dx="6">brellicanworksgroup.com</tspan></text>
  </g>

  <!-- Layout B: black mid band with green sill stripe -->
  <g class="layout layout--band" transform="translate(0,410)">
    <path class="panel-body" d="M22,250 Q40,215 110,205 L240,198 L330,135 Q340,128 360,128 L600,128 Q612,130 615,140 L618,118 Q620,112 640,112 L900,112 Q915,114 918,130 L925,205 L932,210 L932,340 L760,345 A78,78 0 0 0 605,352 L235,355 A80,80 0 0 0 80,345 L30,330 Z"/>
    <path class="glass" d="M268,200 L338,142 L430,140 L430,218 Z M440,140 L590,140 L596,212 L440,218 Z"/>
    <rect class="glass" x="660" y="124" width="212" height="70" rx="8"/>
    <line class="canopy-seam" x1="615" y1="206" x2="925" y2="206"/>
    <g clip-path="url(#ute-side)">
      <rect class="band-black" x="60" y="250" width="880" height="86"/>
      <path class="band-green" d="M230,334 L600,334 Q625,324 650,336 L940,336 L940,352 L230,362 Z"/>
      <circle class="rear-mark" cx="820" cy="300" r="52"/>
    </g>
    <text class="tagline" x="745" y="224" text-anchor="middle">SECURITY &amp; MEDICAL</text>
    <text class="tagline" x="745" y="243" text-anchor="middle">RESPONSE</text>
    <circle class="brand-dot" cx="270" cy="282" r="17"/>
    <text class="brand-name brand-name--light" x="296" y="292" font-size="36">BRELLICAN</text>
    <text class="brand-name brand-name--light" x="298" y="318" font-size="21" letter-spacing="8">WORKS</text>
    <text class="contact-line contact-line--dark" x="252" y="351">1800 392 816 <tspan dx="4">|</tspan><tspan class="contact-web" dx="6">brellicanworksgroup.com</tspan></text>
  </g>
</svg>
</body>
</html>
```